Stationery Design Project for import company - Tallo Goods

We are a import company that sells branded products to large retailers in New Zealand.
We need a simple, professional looking Logo, Business Cards, Email Signature and Letterhead.
Design needs to have some colour in it but nothing too bright or youthful.
The brand is business to business.
The companies name is Tallo Goods.
I have uploaded some examples of business cards that I like
Also need a powerpoint template
The range of products is diverse so the deign needs to be generic. Please note that the business does not sell to consumers only other businesses
Target Market(s)
Buyers at Retail Companies Head Offices (business to business)
Industry/Entity Type
Business
Look and feel
Each slider illustrates characteristics of the customer's brand and the style your logo design should communicate.

```html
<!DOCTYPE html>
<html lang="en">
<head>
<meta charset="utf-8">
<title>Tallo Goods – Stationery</title>
<link rel="stylesheet" href="https://fonts.googleapis.com/css2?family=Arimo:wght@400;700&display=swap">
<style>
:root{
  --bg:#e4e6e8;
  --paper:#ffffff;
  --blue:#1b8fd8;
  --blue-light:#45b0ec;
  --blue-deep:#0d6fb8;
  --navy:#0d3a68;
  --ink:#3a3a3a;
  --muted:#6a6a6a;
}
*{box-sizing:border-box;margin:0;padding:0}
html,body{width:1200px;height:871px;overflow:hidden}
body{background:var(--bg);font-family:"Arimo",Arial,sans-serif;color:var(--ink);position:relative}
.piece{position:absolute;background:var(--paper);overflow:hidden;box-shadow:0 2px 6px rgba(0,0,0,.18)}
.brand{display:flex;align-items:center;gap:10px}
.brand-mark{background:var(--navy);flex:none}
.brand-name{font-family:"Arimo",Arial,sans-serif;font-weight:700;color:var(--navy);white-space:nowrap;letter-spacing:.02em}
.stripe{position:absolute;left:0;right:0;bottom:0;display:flex}
.stripe .dark{background:var(--navy)}
.stripe .gap{background:#fff}
.stripe .light{background:var(--blue-light);flex:1}
.small{font-size:7px;line-height:1.35;color:var(--muted)}

/* envelope */
.envelope{left:68px;top:39px;width:519px;height:376px;background:transparent;box-shadow:none;overflow:visible}
.envelope .flap{position:absolute;left:0;top:0;width:519px;height:135px}
.envelope .body{position:absolute;left:0;top:131px;width:519px;height:245px;background:var(--paper);box-shadow:0 2px 6px rgba(0,0,0,.18);overflow:hidden}
.envelope .brand{position:absolute;left:20px;top:30px}
.envelope .return{position:absolute;left:190px;top:30px}

/* letterhead */
.letterhead{left:657px;top:46px;width:491px;height:689px}
.letterhead .brand{position:absolute;left:128px;top:52px}
.letterhead .recipient{position:absolute;left:70px;top:215px;font-size:8.5px;line-height:1.35}
.letterhead .letter{position:absolute;left:70px;top:327px;width:340px;font-size:8.5px;line-height:1.45}
.letter p{margin-bottom:12px}
.letter .sign-off{margin-top:4px}
.letter .sign-space{height:16px}
.letterhead .footer{position:absolute;right:18px;bottom:42px;text-align:right;font-size:9px;line-height:1.5;color:var(--muted)}

/* cards */
.card-back{left:68px;top:445px;width:251px;height:142px}
.card-back .brand{position:absolute;left:16px;top:20px}
.card-back .details{position:absolute;left:16px;top:66px;font-size:6px}
.card-back .person{position:absolute;left:130px;top:90px}
.person .name{color:var(--blue-deep);font-size:11px}
.person .role{font-size:7.5px;color:var(--muted)}
.card-front{left:365px;top:449px;width:253px;height:138px;background:linear-gradient(135deg,#38a8ea 0%,#1583cf 55%,#0b5fa6 100%)}
.card-front .brand{position:absolute;left:35px;top:56px}
.card-front .brand-mark{background:#fff}
.card-front .brand-name{color:#fff}

/* email signature */
.signature{left:165px;top:623px;width:387px;height:103px;background:linear-gradient(#ffffff,#f0f1f2)}
.signature .brand{position:absolute;left:24px;top:40px}
.signature .person{position:absolute;left:187px;top:20px}
.signature .details{position:absolute;left:187px;top:55px;font-size:6.5px}

/* logo strip */
.logo-strip{left:0;top:769px;width:1200px;height:84px;background:linear-gradient(#f6f7f8,#e9ebed);box-shadow:none}
.logo-strip .brand{position:absolute;left:22px;top:25px;gap:14px}
</style>
</head>
<body>

<div class="piece envelope">
  <svg class="flap" viewBox="0 0 519 135" aria-hidden="true">
    <defs>
      <linearGradient id="flapFill" x1="0" y1="0" x2="0" y2="1">
        <stop offset="0" stop-color="#4db4ef"/>
        <stop offset="1" stop-color="#1680cc"/>
      </linearGradient>
    </defs>
    <path d="M6 6 Q0 6 0 14 L0 135 L519 135 L519 14 Q519 6 513 6 Z" fill="url(#flapFill)"/>
  </svg>
  <div class="body">
    <div class="brand">
      <span class="brand-mark" style="width:22px;height:22px"></span>
      <span class="brand-name" style="font-size:15px">Tallo Goods</span>
    </div>
    <div class="return small">48 Harbour Road, Auckland,<br>1010, New Zealand<br>www.TalloGoods.com</div>
    <div class="stripe" style="height:12px">
      <span class="dark" style="width:445px"></span><span class="gap" style="width:4px"></span><span class="light"></span>
    </div>
  </div>
</div>

<div class="piece letterhead">
  <div class="brand">
    <span class="brand-mark" style="width:30px;height:30px"></span>
    <span class="brand-name" style="font-size:20px">Tallo Goods</span>
  </div>
  <div class="recipient">Name<br>Title<br>Company Name<br>Address<br>City, State, Zip Code</div>
  <div class="letter">
    <p>Dear Mark Holden,</p>
    <p>Thank you for your recent enquiry about our range. We import quality branded goods for retail partners across the country and would be glad to share our current catalogue with your buying team.</p>
    <p>Our product lines cover homeware, personal care, stationery and seasonal items. Each line is sourced from trusted makers and shipped on reliable schedules. We offer flexible order sizes, clear pricing and a dedicated account manager for every client.</p>
    <p>Please let us know a suitable time to meet. We look forward to working with you and supporting your stores this season.</p>
    <div class="sign-off">Sincerely,</div>
    <div class="sign-space"></div>
    <div>Your Name goes here<br>Consultant Manager</div>
  </div>
  <div class="footer">48 Harbour Road, Auckland 1010, New Zealand<br>P : 09 555 0142 &nbsp; C: 000 000 0000 &nbsp; F : 000 000 0000 &nbsp; E : liam@tallogoods.com &nbsp; www.TalloGoods.com</div>
  <div class="stripe" style="height:11px">
    <span class="dark" style="width:352px"></span><span class="gap" style="width:5px"></span><span class="light"></span>
  </div>
</div>

<div class="piece card-back">
  <div class="brand">
    <span class="brand-mark" style="width:18px;height:18px"></span>
    <span class="brand-name" style="font-size:11px">Tallo Goods</span>
  </div>
  <div class="details small">48 Harbour Road, Auckland,<br>1010, New Zealand<br>P : 09 555 0142<br>C : 000 000 0000<br>F : 000 000 0000<br>E : liam@tallogoods.com<br>W : www.TalloGoods.com</div>
  <div class="person"><div class="name">Liam Carver</div><div class="role">President</div></div>
  <div class="stripe" style="height:7px">
    <span class="dark" style="width:178px"></span><span class="gap" style="width:3px"></span><span class="light"></span>
  </div>
</div>

<div class="piece card-front">
  <div class="brand">
    <span class="brand-mark" style="width:22px;height:22px"></span>
    <span class="brand-name" style="font-size:15px">Tallo Goods</span>
  </div>
</div>

<div class="piece signature">
  <div class="brand">
    <span class="brand-mark" style="width:20px;height:20px"></span>
    <span class="brand-name" style="font-size:13px">Tallo Goods</span>
  </div>
  <div class="person"><div class="name">Liam Carver</div><div class="role">President</div></div>
  <div class="details small">48 Harbour Road, Auckland 1010, New Zealand<br>P : 09 555 0142 &nbsp; C : 000 000 0000 &nbsp; F : 000 000 0000<br>E : liam@tallogoods.com<br>www.TalloGoods.com</div>
</div>

<div class="piece logo-strip">
  <div class="brand">
    <span class="brand-mark" style="width:34px;height:34px"></span>
    <span class="brand-name" style="font-size:24px">Tallo Goods</span>
  </div>
</div>

</body>
</html>
```